Fontenot Bayou Grillhouse (Owners Card)

Need a classy, but modern business card. I have included a promotional card for the steakhouse. I need one for myself (the owner) that is more professional.

Target Market(s)

General Public

Industry/Entity Type

Food service

Contact Information for Business Card

Name, business address, phone number, email, logo

Font styles to use
Serif
Sans Serif
Decorative
Script

Requirements
Must have
• My name (Darvel Pruitt), business address (327 Oakmere Street), phone number (510) 493-2615, email (Dpruittkr4@mailvane.example. On the back of the card: Psalms 27 1 The LORD is my light and my salvation— whom shall I fear? The LORD is the stronghold of my life— of whom shall I be afraid? 2 When the wicked advance against me to devour me, it is my enemies and my foes who will stumble and fall. 3 Though an army besiege me, my heart will not fear; though war break out against me, even then I will be confident.
Nice to have
• Something that’s bold, but modern and professional.

```html
<!DOCTYPE html>
<html lang="en">
<head>
<meta charset="utf-8">
<title>Fontenot Bayou Grillhouse – Owner Card</title>
<link rel="stylesheet" href="https://fonts.googleapis.com/css2?family=Montserrat:wght@400;500;700;800&display=swap">
<style>
  :root {
    --bg: #3b3b3d;
    --card-white: #ffffff;
    --card-black: #1c1c1c;
    --band: #1a1a1a;
    --red: #e5161c;
    --ink: #1e1e1e;
    --brand: #e8321a;
    --verse: #ffffff;
  }
  * { box-sizing: border-box; margin: 0; padding: 0; }
  html, body { width: 1200px; height: 1200px; overflow: hidden; }
  body {
    background: var(--bg);
    font-family: "Montserrat", Arial, sans-serif;
    display: flex;
    flex-direction: column;
    align-items: center;
    justify-content: center;
    gap: 60px;
  }
  .card {
    position: relative;
    width: 840px;
    height: 480px;
    border-radius: 34px;
    overflow: hidden;
  }
  .card--front { background: var(--card-white); }
  .card--back { background: var(--card-black); display: flex; align-items: center; justify-content: center; }

  .brand {
    position: absolute;
    top: 120px;
    right: 60px;
    width: 340px;
    text-align: center;
    color: var(--brand);
    font-weight: 700;
    font-size: 34px;
    line-height: 1.15;
  }
  .card--back .brand {
    position: static;
    width: auto;
    font-size: 58px;
  }

  .owner { position: absolute; left: 64px; top: 150px; }
  .owner__name {
    color: var(--red);
    font-weight: 800;
    font-size: 40px;
    letter-spacing: 1px;
    text-transform: uppercase;
  }
  .owner__title {
    color: var(--ink);
    font-weight: 500;
    font-size: 20px;
    letter-spacing: 1px;
    margin: 2px 0 16px 26px;
  }
  .contacts { list-style: none; margin-left: 26px; }
  .contacts li {
    display: flex;
    align-items: center;
    gap: 12px;
    color: var(--ink);
    font-size: 23px;
    font-weight: 500;
    line-height: 1.45;
  }
  .contacts svg { width: 24px; height: 24px; fill: var(--red); flex: none; }

  .verse-band {
    position: absolute;
    left: 0; right: 0;
    top: 360px;
    height: 90px;
    background: var(--band);
    color: var(--verse);
    display: flex;
    flex-direction: column;
    justify-content: center;
    align-items: center;
    font-size: 16px;
    font-weight: 500;
    line-height: 1.5;
  }
</style>
</head>
<body>

<section class="card card--front">
  <div class="brand">Fontenot Bayou Grillhouse</div>

  <div class="owner">
    <h1 class="owner__name">Darvel Pruitt</h1>
    <p class="owner__title">OWNER</p>
    <ul class="contacts">
      <li>
        <svg viewBox="0 0 24 24" aria-hidden="true"><path d="M6.6 10.8a15.1 15.1 0 0 0 6.6 6.6l2.2-2.2c.3-.3.7-.4 1-.2 1.1.4 2.3.6 3.6.6.6 0 1 .4 1 1V20c0 .6-.4 1-1 1A17 17 0 0 1 3 4c0-.6.4-1 1-1h3.5c.6 0 1 .4 1 1 0 1.3.2 2.5.6 3.6.1.3 0 .7-.2 1z"/></svg>
        (510) 493-2615
      </li>
      <li>
        <svg viewBox="0 0 24 24" aria-hidden="true"><path d="M2 5h20v14H2z M3.5 6.5 12 13l8.5-6.5" fill-rule="evenodd"/><path d="M3 6l9 7 9-7" fill="none" stroke="#fff" stroke-width="1.6"/></svg>
        Dpruittkr4@mailvane.example
      </li>
      <li>
        <svg viewBox="0 0 24 24" aria-hidden="true"><path d="M12 2a7 7 0 0 0-7 7c0 5.2 7 13 7 13s7-7.8 7-13a7 7 0 0 0-7-7zm0 9.5A2.5 2.5 0 1 1 12 6.5a2.5 2.5 0 0 1 0 5z"/></svg>
        327 Oakmere Street
      </li>
    </ul>
  </div>

  <div class="verse-band">
    <p>The LORD is my light and my salvation— whom shall I fear?</p>
    <p>The LORD is the stronghold of my life— of whom shall I be afraid?</p>
  </div>
</section>

<section class="card card--back">
  <div class="brand">Fontenot Bayou Grillhouse</div>
</section>

</body>
</html>
```